Luxury organic cosmetics packaging design
Willow Crest Botanics
beautiful inside and out
I am launching with six products for which each will require a recyclable bottle or jar as follows:
Face wash (100ml) - bottle
Body wash (250 ml) - bottle
Toner (200ml) - spray bottle
Serum (30ml) - bottle with pump insert
Face balm (100ml) - Jar
Body Balm (200ml) - jar
Face wash, serum, and face balm will also require a recyclable box design to go with the bottle/jar.
Personal Care
Women aged 25 - 40 who strive to live healthier lives but need that extra push to make the jump. The brand is aiming to make a personal connection with the target market so designs need to be beautiful but practicle at the same time.
I would much prefer shorter packaging with depth rather than tall and thin. I would prefer darker colours but would be open to duck egg or other neutral colours but gender neutral colours are preferred as I don't want to alienate men from the brand. The logo needs to blend well with the packaging and there needs to be adequate space for labelling.

```html
<!DOCTYPE html>
<html lang="en">
<head>
<meta charset="utf-8">
<title>Willow Crest Botanics — Packaging Range</title>
<link rel="stylesheet" href="https://fonts.googleapis.com/css2?family=Cinzel:wght@500&family=Roboto:wght@400&display=swap">
<style>
  :root {
    --bg: #ffffff;
    --gold: #c9a24a;
    --amber-dark: #4a2408;
    --amber-mid: #8a4a12;
    --amber-light: #b8691f;
    --black: #0d0d0d;
    --black-soft: #2a2a2a;
    --label-text: #f2f2f2;
  }
  html, body {
    margin: 0;
    padding: 0;
    width: 1200px;
    height: 926px;
    overflow: hidden;
    background: var(--bg);
  }
  .range {
    display: block;
    width: 1200px;
    height: 926px;
  }
  .brand-name {
    font-family: "Cinzel", serif;
    font-weight: 500;
    fill: var(--gold);
    letter-spacing: 1px;
  }
  .product-name {
    font-family: "Roboto", sans-serif;
    fill: var(--label-text);
  }
  .net-weight {
    font-family: "Roboto", sans-serif;
    fill: var(--label-text);
    letter-spacing: 0.3px;
  }
  .gold-rule {
    stroke: var(--gold);
    stroke-width: 2;
  }
</style>
</head>
<body>
<svg class="range" viewBox="0 0 1200 926" xmlns="http://www.w3.org/2000/svg" aria-label="Willow Crest Botanics product range: body balm jar, toner spray bottle and face wash tube">
  <defs>
    <linearGradient id="amberGlass" x1="0" x2="1" y1="0" y2="0">
      <stop offset="0" stop-color="var(--amber-dark)"/>
      <stop offset="0.25" stop-color="var(--amber-light)"/>
      <stop offset="0.6" stop-color="var(--amber-mid)"/>
      <stop offset="1" stop-color="var(--amber-dark)"/>
    </linearGradient>
    <linearGradient id="blackGloss" x1="0" x2="1" y1="0" y2="0">
      <stop offset="0" stop-color="#000"/>
      <stop offset="0.3" stop-color="var(--black-soft)"/>
      <stop offset="0.65" stop-color="var(--black)"/>
      <stop offset="1" stop-color="#000"/>
    </linearGradient>
    <linearGradient id="tubeMatte" x1="0" x2="1" y1="0" y2="0">
      <stop offset="0" stop-color="#1a1a1a"/>
      <stop offset="0.4" stop-color="#3a3a3a"/>
      <stop offset="1" stop-color="#151515"/>
    </linearGradient>
  </defs>

  <!-- Body balm jar -->
  <g class="product product--jar">
    <rect class="jar-body" x="83" y="468" width="500" height="437" rx="18" fill="url(#amberGlass)"/>
    <rect class="jar-lid" x="98" y="370" width="470" height="104" rx="10" fill="url(#blackGloss)"/>
    <text class="brand-name" x="333" y="672" font-size="25" text-anchor="middle" textLength="340">WILLOW CREST BOTANICS</text>
    <line class="gold-rule" x1="118" y1="722" x2="548" y2="722"/>
    <line class="gold-rule" x1="118" y1="745" x2="548" y2="745"/>
    <text class="product-name" x="333" y="800" font-size="17" text-anchor="middle">Body Balm</text>
    <line class="gold-rule" x1="118" y1="815" x2="548" y2="815"/>
    <text class="net-weight" x="333" y="840" font-size="11" text-anchor="middle">NET WT 6.8 OZ (200ml)</text>
  </g>

  <!-- Toner spray bottle -->
  <g class="product product--spray">
    <rect class="spray-cap" x="655" y="325" width="98" height="130" rx="8" fill="url(#blackGloss)"/>
    <path class="spray-bottle" d="M640 455 H768 Q790 462 790 500 V895 Q790 907 778 907 H630 Q618 907 618 895 V500 Q618 462 640 455 Z" fill="url(#blackGloss)"/>
    <text class="brand-name" x="704" y="668" font-size="19" text-anchor="middle">WILLOW CREST</text>
    <text class="brand-name" x="704" y="694" font-size="19" text-anchor="middle">BOTANICS</text>
    <line class="gold-rule" x1="632" y1="725" x2="776" y2="725"/>
    <text class="product-name" x="704" y="822" font-size="14" text-anchor="middle">Toner</text>
    <line class="gold-rule" x1="632" y1="840" x2="776" y2="840"/>
    <text class="net-weight" x="704" y="872" font-size="10" text-anchor="middle">NET WT 6.8 OZ (200ml)</text>
  </g>

  <!-- Face wash tube -->
  <g class="product product--tube">
    <path class="tube-body" d="M820 20 H1112 L1104 40 Q1090 420 1062 778 H846 Q818 420 828 40 Z" fill="url(#tubeMatte)"/>
    <rect class="tube-cap" x="848" y="775" width="212" height="125" rx="8" fill="url(#blackGloss)"/>
    <text class="brand-name" x="966" y="505" font-size="23" text-anchor="middle">WILLOW CREST</text>
    <text class="brand-name" x="966" y="536" font-size="23" text-anchor="middle">BOTANICS</text>
    <line class="gold-rule" x1="862" y1="622" x2="1070" y2="622"/>
    <text class="product-name" x="1050" y="672" font-size="14" text-anchor="end">Face Wash</text>
    <line class="gold-rule" x1="862" y1="712" x2="1070" y2="712"/>
    <text class="net-weight" x="966" y="740" font-size="10" text-anchor="middle">NET WT 3.4 OZ (100ml)</text>
  </g>
</svg>
</body>
</html>
```